Real Estate - Large Sign Design

I am looking for a fresh new look for our leasing signs that will be showcase in front of commercial buildings available for lease. The sign dimension can be either 8'x4' or 4'x8'. They must exemplify our brand (see attachments) and be very visible by people driving by at high speeds.
They must include the following:
- Our logo (vector attached)
- Office Space Available
- 555-018-3274
- Nell Ruby
- Carl Ivey
- www.vantorile.com
Please let me know if you have any questions.
Target Market(s)
Drivers in high traffic areas, walking crowds
Industry/Entity Type
Real Estate
Requirements
Must have
- They must include the following:
- - Our logo (vector attached)
- - Office Space Available
- - 555-018-3274
- - Nell Ruby
- - Carl Ivey
- - www.vantorile.com
Should not have
- Should not be busy or hard to read.

```html
<!DOCTYPE html>
<html lang="en">
<head>
<meta charset="utf-8">
<title>Office Space Available – Leasing Sign</title>
<link rel="stylesheet" href="https://fonts.googleapis.com/css2?family=Roboto+Condensed:wght@700&family=Roboto:ital,wght@0,500;0,700;1,400&display=swap">
<style>
  :root {
    --backdrop: #8c8c8c;
    --sign-white: #ffffff;
    --ink: #0d0d0d;
    --brand-green: #2f8c63;
    --agent-slate: #3f5a56;
    --slate-top: #4a5a66;
    --green-mid: #3f8f6a;
    --green-deep: #12a55a;
    --lime: #b9d45e;
    --green-band: #4cb870;
    --logo-white: #ffffff;
  }
  html, body {
    margin: 0;
    width: 1200px;
    height: 791px;
    overflow: hidden;
    background: var(--backdrop);
  }
  .leasing-sign {
    position: absolute;
    left: 50px;
    top: 120px;
    width: 1100px;
    height: 550px;
    display: block;
  }
  .sign-face { fill: var(--sign-white); }
  .headline {
    font-family: "Roboto Condensed", "Arial Narrow", sans-serif;
    font-weight: 700;
    font-size: 160px;
    fill: var(--ink);
  }
  .headline-accent {
    font-family: "Roboto", Arial, sans-serif;
    font-weight: 700;
    font-size: 120px;
    letter-spacing: 4px;
    fill: var(--brand-green);
  }
  .agent-names {
    font-family: "Roboto Condensed", "Arial Narrow", sans-serif;
    font-weight: 700;
    font-size: 44px;
    fill: var(--agent-slate);
  }
  .agent-phone {
    font-family: "Roboto", Arial, sans-serif;
    font-weight: 700;
    font-size: 74px;
    fill: var(--ink);
  }
  .agent-web {
    font-family: "Roboto", Arial, sans-serif;
    font-style: italic;
    font-weight: 400;
    font-size: 31px;
    fill: var(--ink);
  }
  .company-name {
    font-family: "Roboto", Arial, sans-serif;
    font-weight: 500;
    font-size: 27px;
    fill: var(--logo-white);
  }
</style>
</head>
<body>
<svg class="leasing-sign" viewBox="0 0 1100 550" role="img" aria-label="Office space available leasing sign">
  <defs>
    <linearGradient id="corner-wedge" x1="0" y1="0" x2="0" y2="1">
      <stop offset="0" stop-color="var(--slate-top)"/>
      <stop offset="0.45" stop-color="var(--green-mid)"/>
      <stop offset="1" stop-color="var(--green-deep)"/>
    </linearGradient>
    <linearGradient id="base-band" x1="0" y1="0" x2="1" y2="0">
      <stop offset="0" stop-color="var(--lime)"/>
      <stop offset="1" stop-color="var(--green-band)"/>
    </linearGradient>
  </defs>

  <rect class="sign-face" x="0" y="0" width="1100" height="550"/>

  <polygon class="base-band" fill="url(#base-band)" points="0,543 1100,384 1100,550 0,550"/>
  <polygon class="corner-wedge" fill="url(#corner-wedge)" points="1090,0 1100,0 1100,550 848,550"/>
  <polygon class="corner-overlap" fill="var(--green-deep)" opacity="0.55" points="950,362 1100,384 1100,550 848,550"/>

  <text class="headline" x="37" y="166" textLength="937" lengthAdjust="spacingAndGlyphs">OFFICE SPACE</text>
  <text class="headline-accent" x="40" y="278" textLength="632" lengthAdjust="spacingAndGlyphs">AVAILABLE</text>

  <text class="agent-names" x="40" y="363">NELL RUBY &amp; CARL IVEY</text>
  <text class="agent-phone" x="37" y="437" textLength="466" lengthAdjust="spacingAndGlyphs">555-018-3274</text>
  <text class="agent-web" x="40" y="474">www.vantorile.com</text>

  <text class="company-name" x="904" y="448">Harwell</text>
  <text class="company-name" x="904" y="477">Estate</text>
  <text class="company-name" x="904" y="506">Group</text>
</svg>
</body>
</html>
```